Want a package created for a new protein bar

We would like a new package created for a new protein bar project The name of the bar will be VOLMBite a real food protein bar, we would like a ‘window’ on the package of bar like Brave Meadow bar below in images.

VOLMBite
‘Super Food Bar’
14g of Whey Protein
The package film size is the following 12cm width x 15cm Length,
Flavor Peanut Chocolate Chip, additional information will be attached shortly like nutrition facts,

Target Market(s)

fitness market, bodybuilders, athletes, everyday people

Industry/Entity Type

Health Product

Logo Text

VOLMBite

Font styles to use
Serif
Sans Serif
Decorative

Requirements
Must have
• Package window

```html
<!DOCTYPE html>
<html lang="en">
<head>
<meta charset="utf-8">
<title>VOLMBite Wrapper – Front and Back</title>
<link href="https://fonts.googleapis.com/css2?family=Rubik:wght@800;900&family=Electrolize&family=Archivo+Narrow:wght@400;700&display=swap" rel="stylesheet">
<style>
  :root {
    --stage: #000000;
    --wrapper-red: #b01f26;
    --seal-gold: #c8aa68;
    --logo-peach: #f6bd73;
    --accent-orange: #f9a634;
    --claim-cream: #f8d9a6;
    --panel-cream: #e6cf9b;
    --label-paper: #efe5cf;
    --label-ink: #6b6252;
    --window-light: #d9a35a;
    --window-dark: #7a4a22;
  }
  * { margin: 0; padding: 0; box-sizing: border-box; }
  html, body {
    width: 1200px; height: 1138px; overflow: hidden;
    background: var(--stage);
  }
  .canvas { position: relative; width: 1200px; height: 1138px; }

  .wrapper { position: absolute; width: 215px; height: 516px; }
  .wrapper--front { left: 328px; top: 310px; }
  .wrapper--back { left: 656px; top: 311px; }
  .wrapper__film { position: absolute; inset: 0; }

  .brand {
    position: absolute; left: 0; right: 0; top: 93px;
    text-align: center;
    font: 900 33px/1 "Rubik", sans-serif;
    color: var(--logo-peach);
    letter-spacing: 0.5px;
  }
  .claim {
    position: absolute; left: 0; right: 0; top: 169px;
    text-align: center;
    font: 15px/17px "Electrolize", sans-serif;
    color: var(--claim-cream);
  }
  .product-window {
    position: absolute; left: 8px; top: 249px; width: 200px; height: 141px;
    background: radial-gradient(ellipse at 45% 55%, var(--window-light) 0%, #b77a3a 55%, var(--window-dark) 100%);
  }
  .flavor {
    position: absolute; left: 0; right: 0; top: 443px;
    text-align: center;
    font: 800 15px/1 "Rubik", sans-serif;
    color: var(--accent-orange);
  }

  .ingredients {
    position: absolute; left: 20px; right: 18px; top: 68px;
    text-align: center;
    font: 11.6px/12.8px "Electrolize", sans-serif;
    color: var(--accent-orange);
  }
  .facts-panel {
    position: absolute; left: 35px; top: 203px; width: 146px; height: 232px;
    background: var(--panel-cream); border-radius: 8px;
  }
  .facts-label {
    position: absolute; left: 11px; top: 13px; width: 122px; height: 204px;
    background: var(--label-paper);
    border: 1px solid #d8cbae;
    padding: 4px 5px 0;
    font-family: "Archivo Narrow", sans-serif;
    color: var(--label-ink);
  }
  .facts-label__inner { border: 0.5px solid #b9ad95; height: 194px; padding: 0 3px; margin: -1px -2px; }
  .facts-title { font: 700 13px/13px "Archivo Narrow", sans-serif; white-space: nowrap; letter-spacing: 0.2px; }
  .facts-row { font-size: 6px; line-height: 7.6px; border-bottom: 0.5px solid #b9ad95; white-space: nowrap; display: flex; justify-content: space-between; }
  .facts-row--plain { border-bottom: none; }
  .facts-row--bold { font-weight: 700; }
  .facts-row--indent { padding-left: 8px; }
  .facts-row--right { justify-content: flex-end; font-weight: 700; font-size: 4.5px; }
  .facts-rule { height: 6px; background: var(--label-ink); margin: 1px 0 2px; }
  .facts-rule--thin { height: 3px; }
  .facts-note { font-size: 3.6px; line-height: 6px; white-space: nowrap; margin-top: 5px; }

  .company {
    position: absolute; left: 0; right: 0; top: 447px;
    text-align: center;
    font: 12px/13px "Electrolize", sans-serif;
    color: var(--accent-orange);
  }
</style>
</head>
<body>
<main class="canvas">

  <section class="wrapper wrapper--front" aria-label="Wrapper front">
    <svg class="wrapper__film" width="215" height="516" viewBox="0 0 215 516">
      <path d="M2 28 C10 150 7 380 2 488 L213 488 C208 380 205 150 213 28 Z" fill="var(--wrapper-red)"/>
      <rect x="0" y="0" width="215" height="28" fill="var(--seal-gold)"/>
      <rect x="0" y="488" width="215" height="28" fill="var(--seal-gold)"/>
    </svg>
    <h1 class="brand">VOLMBite</h1>
    <p class="claim">Super Food Bar<br>14g Whey Protein</p>
    <div class="product-window" role="img" aria-label="Window showing the oat, peanut and chocolate chip bar inside"></div>
    <p class="flavor">Peanut Chocolate Chip</p>
  </section>

  <section class="wrapper wrapper--back" aria-label="Wrapper back">
    <svg class="wrapper__film" width="215" height="516" viewBox="0 0 215 516">
      <path d="M2 28 C10 150 7 380 2 488 L213 488 C208 380 205 150 213 28 Z" fill="var(--wrapper-red)"/>
      <rect x="0" y="0" width="215" height="28" fill="var(--seal-gold)"/>
      <rect x="0" y="488" width="215" height="28" fill="var(--seal-gold)"/>
    </svg>
    <p class="ingredients">INGREDIENTS: Lorem ipsum dolor sit amet, consectetuer adipiscing elit, sed diam nonummy nibh euismod tincidunt ut</p>

    <div class="facts-panel">
      <div class="facts-label">
        <div class="facts-label__inner">
          <div class="facts-title">Nutrition Facts</div>
          <div class="facts-row facts-row--plain">Serving Size</div>
          <div class="facts-row facts-row--plain">Servings Per Container</div>
          <div class="facts-rule"></div>
          <div class="facts-row facts-row--bold" style="font-size:4.5px">Amount Per Serving</div>
          <div class="facts-row facts-row--plain"><b>Calories</b><span>Calories from Fat&nbsp;&nbsp;&nbsp;</span></div>
          <div class="facts-rule facts-rule--thin"></div>
          <div class="facts-row facts-row--right">% Daily Value*</div>
          <div class="facts-row facts-row--bold">Total Fat</div>
          <div class="facts-row facts-row--indent">Saturated Fat</div>
          <div class="facts-row facts-row--indent">Trans Fat</div>
          <div class="facts-row facts-row--bold">Cholesterol</div>
          <div class="facts-row facts-row--bold">Sodium</div>
          <div class="facts-row facts-row--bold">Total Carbohydrate</div>
          <div class="facts-row facts-row--indent">Dietary Fiber</div>
          <div class="facts-row facts-row--indent">Sugars</div>
          <div class="facts-row facts-row--bold facts-row--plain">Protein</div>
          <div class="facts-rule"></div>
          <div class="facts-row">Vitamin</div>
          <div class="facts-note">*Percent Daily Values are based on a 2,000 calorie diet.</div>
        </div>
      </div>
    </div>

    <p class="company">COMPANY NAME<br>Company Address</p>
  </section>

</main>
</body>
</html>
```